Sports Management Agency Website Design

Need a website design for a sports management agency with services as outlined in attached document.

Will need links to social media, section for partners, and ability for member/partner login.

Branding already established refer to attached files.

Look and feel professional consulting/agency, not too sporty.

Similar competitor businesses are all other sports agents.
Updates

Hi, Thanks for the efforts so far. Please don't use too much orange on the site, it is great in the logo, but would prefer darker colours that contrast with the Orange. Cheers Owen

Industry/Entity Type

Media

Number of Pages Required

1 page

Font styles to use
Sans Serif

Requirements
Must have
• See above and brief file....reference existing logo attached.

```html
<!DOCTYPE html>
<html lang="en">
<head>
<meta charset="utf-8">
<title>Kestrel Sports Management</title>
<link rel="stylesheet" href="https://fonts.googleapis.com/css2?family=Open+Sans:wght@300;400;600;700&display=swap">
<style>
:root{
  --orange:#f26a0b;
  --navy:#08087c;
  --ink:#1d1d1d;
  --muted:#8a8f90;
  --band:#e8eeee;
  --white:#ffffff;
  --footer-text:#8b8bc4;
}
*{box-sizing:border-box;margin:0;padding:0}
html,body{width:1200px;height:1200px;overflow:hidden}
body{font-family:"Open Sans",Arial,sans-serif;background:var(--white);color:var(--ink);position:relative}
.site-header{position:absolute;top:0;left:0;width:1200px;height:117px;background:var(--white)}
.brand{position:absolute;left:50px;top:38px;display:flex;align-items:center;gap:10px}
.brand-mark{width:26px;height:26px;border-radius:50%;background:var(--orange)}
.brand-name{font-size:22px;font-weight:700;color:var(--navy);line-height:1.05;width:170px}
.main-nav{position:absolute;top:51px;left:574px;display:flex;gap:0}
.main-nav a{font-size:16px;color:var(--ink);text-decoration:none;margin-right:22px;letter-spacing:.2px}
.main-nav a.is-active{color:var(--orange)}
.social{position:absolute;top:45px;left:967px;display:flex;gap:13px}
.social a{display:block;width:32px;height:32px}
.social .tw{background:#1da1e2}
.social .fb{background:#3b5a9a}
.login-btn{position:absolute;left:1055px;top:45px;width:94px;height:32px;background:var(--orange);border-radius:3px;color:var(--white);font-size:16px;display:flex;align-items:center;justify-content:center;gap:8px;text-decoration:none}
.hero{position:absolute;top:117px;left:0;width:1200px;height:421px;overflow:hidden}
.hero-photo{position:absolute;inset:0;background:
  linear-gradient(180deg,#3c4a5e 0%,#7d8aa8 18%,#2b3039 40%,#3f6a2c 62%,#2f6a25 78%,#23251f 100%)}
.hero-shade{position:absolute;inset:0;background:linear-gradient(90deg,rgba(0,0,0,.45),rgba(0,0,0,0) 60%)}
.hero-title{position:absolute;left:121px;top:178px;font-size:52px;font-weight:300;color:var(--white);line-height:46px}
.hero-sub{position:absolute;left:121px;top:287px;font-size:22px;font-weight:300;color:var(--white)}
.hero-arrow{position:absolute;top:190px}
.hero-arrow.prev{left:48px}
.hero-arrow.next{left:1126px}
.content-band{position:absolute;top:538px;left:0;width:1200px;height:597px;background:var(--band)}
.section-title{position:absolute;top:28px;width:1200px;text-align:center;font-size:28px;font-weight:400;color:var(--ink)}
.section-sub{position:absolute;top:64px;width:1200px;text-align:center;font-size:16px;font-weight:300;color:var(--muted)}
.services{position:absolute;top:115px;left:50px;display:flex;gap:5px}
.service-card{width:271px;height:209px;color:var(--white);text-align:center;padding-top:36px}
.service-card.orange{background:var(--orange)}
.service-card.navy{background:var(--navy)}
.service-card svg{display:block;margin:0 auto;height:64px}
.service-card h3{font-size:19px;font-weight:600;margin-top:18px}
.service-card p{font-size:14px;line-height:18px;margin-top:10px}
.dots{position:absolute;top:342px;left:575px;display:flex;gap:8px}
.dots span{width:12px;height:12px;border-radius:50%;background:#a3a7a9}
.dots span.is-active{background:var(--orange)}
.block-title{position:absolute;top:390px;font-size:22px;font-weight:400;color:var(--ink)}
.about{left:50px}
.partners{left:620px}
.about-text{position:absolute;left:49px;top:427px;width:528px;font-size:14px;line-height:24px;text-align:justify;color:var(--ink)}
.partner-logos{position:absolute;left:623px;top:435px;display:flex;gap:19px}
.partner-logos div{width:117px;height:77px;background:var(--white);display:flex;align-items:center;justify-content:center;font-size:22px;color:#c9cccd}
.site-footer{position:absolute;top:1135px;left:0;width:1200px;height:65px;background:var(--navy);color:var(--footer-text);font-size:14px}
.copyright{position:absolute;left:49px;top:20px}
.footer-links{position:absolute;right:51px;top:20px}
.footer-links span{margin:0 4px}
</style>
</head>
<body>
<header class="site-header">
  <div class="brand">
    <span class="brand-mark"></span>
    <span class="brand-name">Kestrel Sports Management</span>
  </div>
  <nav class="main-nav">
    <a class="is-active" href="#">HOME</a>
    <a href="#">ABOUT US</a>
    <a href="#">SERVICES</a>
    <a href="#">CONTACT US</a>
  </nav>
  <div class="social">
    <a class="tw" href="#" aria-label="Social network link"></a>
    <a class="fb" href="#" aria-label="Social network link"></a>
  </div>
  <a class="login-btn" href="#">
    <svg width="14" height="18" viewBox="0 0 14 18"><path d="M3 8V5a4 4 0 0 1 8 0v3" fill="none" stroke="#f9c38c" stroke-width="2"/><rect x="1" y="8" width="12" height="9" rx="1" fill="#f9c38c"/></svg>
    Login
  </a>
</header>

<section class="hero">
  <div class="hero-photo" role="img" aria-label="Floodlit football stadium full of spectators"></div>
  <div class="hero-shade"></div>
  <svg class="hero-arrow prev" width="26" height="44" viewBox="0 0 26 44"><path d="M22 2 4 22l18 20" fill="none" stroke="#fff" stroke-opacity=".75" stroke-width="3"/></svg>
  <h1 class="hero-title">Some heading<br>comes here</h1>
  <p class="hero-sub">Contrary to popular belief, Lorem Ipsum is not</p>
  <svg class="hero-arrow next" width="26" height="44" viewBox="0 0 26 44"><path d="M4 2l18 20L4 42" fill="none" stroke="#fff" stroke-opacity=".75" stroke-width="3"/></svg>
</section>

<main class="content-band">
  <h2 class="section-title">SERVICES WE OFFER</h2>
  <p class="section-sub">Contrary to popular belief, Lorem Ipsum is not</p>

  <div class="services">
    <article class="service-card orange">
      <svg viewBox="0 0 64 64" width="64"><path d="M32 3l8.5 19.5 21 2-16 14 4.8 20.7L32 48.5 13.7 59.2l4.8-20.7-16-14 21-2z" fill="none" stroke="#fff" stroke-width="2.5" stroke-linejoin="round"/></svg>
      <h3>Sponsorship</h3>
      <p>Contrary to popular belief, Lorem<br>Ipsum is not&nbsp; Contrary to popular</p>
    </article>
    <article class="service-card navy">
      <svg viewBox="0 0 78 56" width="78"><rect x="2" y="2" width="74" height="52" rx="4" fill="none" stroke="#fff" stroke-width="2.5"/><circle cx="22" cy="22" r="8" fill="none" stroke="#fff" stroke-width="2.5"/><path d="M9 45c0-9 6-13 13-13s13 4 13 13z" fill="none" stroke="#fff" stroke-width="2.5"/><path d="M44 18h24M44 27h24M44 36h18" stroke="#fff" stroke-width="2.5"/></svg>
      <h3>Personal Brand Strategy</h3>
      <p>Contrary to popular belief, Lorem<br>Ipsum is not&nbsp; Contrary to popular</p>
    </article>
    <article class="service-card orange">
      <svg viewBox="0 0 74 64" width="74"><rect x="2" y="12" width="70" height="50" fill="none" stroke="#fff" stroke-width="2.5"/><path d="M27 12V3h20v9M14 12v50M25 12v50M37 12v50M49 12v50M60 12v50" fill="none" stroke="#fff" stroke-width="2.5"/></svg>
      <h3>Employment</h3>
      <p>Contrary to popular belief, Lorem<br>Ipsum is not&nbsp; Contrary to popular</p>
    </article>
    <article class="service-card navy">
      <svg viewBox="0 0 80 56" width="80"><g fill="none" stroke="#fff" stroke-width="2.5"><circle cx="22" cy="17" r="9"/><circle cx="58" cy="17" r="9"/><path d="M3 48c0-10 7-16 17-16M77 48c0-10-7-16-17-16"/><circle cx="40" cy="20" r="11"/><path d="M18 54c0-13 10-20 22-20s22 7 22 20z"/></g></svg>
      <h3>Team Development</h3>
      <p>Contrary to popular belief, Lorem<br>Ipsum is not&nbsp; Contrary to popular</p>
    </article>
  </div>

  <div class="dots"><span class="is-active"></span><span></span><span></span></div>

  <h2 class="block-title about">WHO WE ARE?</h2>
  <p class="about-text">There are many variations of passages of Lorem Ipsum available, but the majority have suffered alteration in some form, by injected humour, or randomised words which don't look even slightly believable. If you are going to use a passage of Lorem Ipsum, you need to be sure there isn't anything embarrassing hidden in the middle of text.</p>

  <h2 class="block-title partners">OUR PARTMERS</h2>
  <div class="partner-logos">
    <div>Logo</div><div>Logo</div><div>Logo</div><div>Logo</div>
  </div>
</main>

<footer class="site-footer">
  <span class="copyright">Copyright note</span>
  <span class="footer-links">Home<span>|</span>Contact us</span>
</footer>
</body>
</html>
```